Evergold Fernbark Inc

Industry/Entity Type

Forestry

Contact Information for Business Card

Company name: Evergold Fernbark INC, Contact Info: Rovelio Marquin, Phone # 208 555 0187, Addres: 284 Willowbend Creek Rd, Larchmere VT 05999, Email: evergoldfernbark@mailbrook.net

```html
<!DOCTYPE html>
<html lang="en">
<head>
<meta charset="utf-8">
<title>Evergold Fernbark INC – Business Card</title>
<link rel="stylesheet" href="https://fonts.googleapis.com/css2?family=Montserrat:wght@400;500;600&display=swap">
<style>
  :root {
    --bg: #e6e7e8;
    --card: #ffffff;
    --navy: #233545;
    --green: #7db23f;
    --text: #1f2f3d;
  }
  * { box-sizing: border-box; margin: 0; padding: 0; }
  html, body { width: 1200px; height: 859px; overflow: hidden; }
  body {
    background: var(--bg);
    font-family: "Montserrat", sans-serif;
    color: var(--text);
    display: flex;
    align-items: center;
    justify-content: center;
    gap: 40px;
  }
  .card {
    position: relative;
    width: 540px;
    height: 309px;
    background: var(--card);
    box-shadow: 0 10px 28px rgba(0,0,0,0.14);
    overflow: hidden;
  }
  /* Front */
  .card-front {
    display: flex;
    flex-direction: column;
    align-items: center;
    justify-content: center;
    gap: 18px;
  }
  .brand-dot {
    width: 34px;
    height: 34px;
    border-radius: 50%;
    background: var(--green);
  }
  .brand-name {
    font-size: 26px;
    font-weight: 600;
    color: var(--navy);
    letter-spacing: 0.5px;
  }
  /* Back */
  .card-waves { position: absolute; inset: 0; width: 100%; height: 100%; }
  .contact {
    position: absolute;
    left: 52px;
    top: 78px;
  }
  .contact-name {
    font-size: 31px;
    font-weight: 500;
    letter-spacing: 1px;
    color: var(--text);
  }
  .contact-rule {
    width: 38px;
    height: 3px;
    background: var(--green);
    margin: 14px 0 16px;
  }
  .contact-list { list-style: none; }
  .contact-item {
    display: flex;
    align-items: flex-start;
    gap: 10px;
    font-size: 15px;
    font-weight: 500;
    line-height: 21px;
    margin-bottom: 4px;
    letter-spacing: 0.4px;
  }
  .contact-icon {
    flex: none;
    width: 18px;
    height: 18px;
    margin-top: 2px;
  }
</style>
</head>
<body>
  <section class="card card-front">
    <span class="brand-dot"></span>
    <span class="brand-name">Evergold Fernbark INC</span>
  </section>

  <section class="card card-back">
    <svg class="card-waves" viewBox="0 0 540 309" preserveAspectRatio="none" aria-hidden="true">
      <path fill="var(--green)" d="M330 0 L540 0 L540 309 L480 309 C440 290 420 250 415 200 C410 140 420 80 392 42 C376 20 356 6 330 0Z"/>
      <path fill="var(--navy)" d="M405 0 L540 0 L540 230 C500 236 470 222 456 192 C436 150 446 100 436 62 C428 32 416 12 405 0Z"/>
    </svg>

    <div class="contact">
      <h1 class="contact-name">Rovelio Marquin</h1>
      <div class="contact-rule"></div>
      <ul class="contact-list">
        <li class="contact-item">
          <svg class="contact-icon" viewBox="0 0 18 18" aria-hidden="true">
            <circle cx="9" cy="9" r="9" fill="var(--green)"/>
            <path fill="#fff" d="M6.2 4.6 L7.6 6.6 L6.8 7.6 C7.4 8.9 8.6 10.2 10 10.9 L11 10.1 L13.2 11.4 L12.4 13 C9 13 5 9 5 5.5Z"/>
          </svg>
          <span>208 555 0187</span>
        </li>
        <li class="contact-item">
          <svg class="contact-icon" viewBox="0 0 18 18" aria-hidden="true">
            <circle cx="9" cy="9" r="9" fill="var(--green)"/>
            <rect x="4.5" y="6" width="9" height="6.4" fill="none" stroke="#fff" stroke-width="1.2"/>
            <path d="M4.5 6 L9 9.6 L13.5 6" fill="none" stroke="#fff" stroke-width="1.2"/>
          </svg>
          <span>evergoldfernbark@mailbrook.net</span>
        </li>
        <li class="contact-item">
          <svg class="contact-icon" viewBox="0 0 18 18" aria-hidden="true">
            <circle cx="9" cy="9" r="9" fill="var(--green)"/>
            <path fill="#fff" d="M9 3.8 C6.9 3.8 5.4 5.3 5.4 7.3 C5.4 9.8 9 14 9 14 C9 14 12.6 9.8 12.6 7.3 C12.6 5.3 11.1 3.8 9 3.8Z"/>
            <circle cx="9" cy="7.3" r="1.4" fill="var(--green)"/>
          </svg>
          <span>284 Willowbend Creek Rd,<br>Larchmere VT 05999</span>
        </li>
      </ul>
    </div>
  </section>
</body>
</html>
```